Redfern Espresso Branding
Business Cards & Stationary Set
Professional
Dale Ostrander
Manager
1875 Heron Ridge Ave.
Pine Hollow, MN. 55990
r_fern@quillpost.net
I would like rounded corners on the business cards
Drive-thru to receive one free 12 oz. drink of choice!

```html
<!DOCTYPE html>
<html lang="en">
<head>
<meta charset="utf-8">
<title>Redfern Espresso Stationery</title>
<link href="https://fonts.googleapis.com/css2?family=Open+Sans:wght@400;600;700&family=Roboto+Condensed:wght@700&display=swap" rel="stylesheet">
<style>
  :root{
    --bg:#d6ccb8;
    --paper:#f4f0e4;
    --paper-shade:#e8e2d2;
    --orange:#c8602e;
    --green:#4d5a43;
    --green-soft:#8f9a7c;
    --ink:#6b6558;
  }
  *{box-sizing:border-box;margin:0;padding:0}
  html,body{width:1200px;height:890px;overflow:hidden;background:var(--bg);font-family:"Open Sans",sans-serif;color:var(--ink)}
  .canvas{position:relative;width:1200px;height:890px}
  .sheet{position:absolute;background:linear-gradient(90deg,var(--paper) 0%,var(--paper) 60%,var(--paper-shade) 100%);box-shadow:0 4px 14px rgba(60,45,20,.25)}
  .brand{display:flex;align-items:center;gap:6px;font-weight:700;color:var(--green);text-transform:uppercase;letter-spacing:.5px}
  .brand-square{background:var(--orange);flex:none}
  .contact{font-size:8px;line-height:12px;color:var(--ink)}
  .promo{font-family:"Roboto Condensed",sans-serif;font-weight:700;text-transform:uppercase;letter-spacing:.4px}
  .trees{position:absolute;background:linear-gradient(90deg,var(--orange) 0 35%,var(--green) 35% 70%,var(--green-soft) 70%)}

  /* letterhead */
  .letterhead{left:60px;top:60px;width:408px;height:730px}
  .letterhead .brand{position:absolute;left:40px;top:36px;font-size:11px;width:90px;flex-wrap:wrap}
  .letterhead .brand-square{width:22px;height:22px}
  .letterhead .contact{position:absolute;left:200px;top:34px}
  .letterhead .trees{right:40px;bottom:28px;width:56px;height:46px}
  .letterhead .promo{position:absolute;left:0;right:0;bottom:0;height:22px;border-top:2px solid var(--orange);padding:4px 18px;font-size:11px;color:var(--orange)}

  /* envelope */
  .envelope{left:476px;top:240px;width:586px;height:350px;background:none;box-shadow:none}
  .envelope svg.body{position:absolute;inset:0;filter:drop-shadow(0 4px 8px rgba(60,45,20,.25))}
  .envelope .brand{position:absolute;left:30px;top:130px;font-size:11px;width:92px;flex-wrap:wrap}
  .envelope .brand-square{width:22px;height:22px}
  .envelope .contact{position:absolute;left:30px;top:190px}
  .envelope .quote{position:absolute;left:350px;top:100px;display:flex;gap:4px;align-items:flex-start}
  .envelope .q{font-family:Georgia,serif;font-size:40px;line-height:30px;color:var(--orange)}
  .envelope .promo{font-size:11px;line-height:13px;color:var(--green);margin-top:6px;width:140px}
  .envelope .trees{right:32px;bottom:48px;width:62px;height:50px}
  .envelope .rule{position:absolute;left:0;right:0;bottom:26px;height:6px;background:var(--green)}

  /* business cards */
  .card{top:612px;width:216px;height:124px;border-radius:10px;overflow:hidden}
  .card-front{left:600px}
  .card-front .brand{position:absolute;left:14px;top:22px;font-size:8px;width:70px;flex-wrap:wrap}
  .card-front .brand-square{width:16px;height:16px}
  .card-front .person{position:absolute;left:96px;top:22px}
  .card-front .name{font-size:8px;font-weight:700;color:var(--orange);text-transform:uppercase}
  .card-front .role{font-size:7px;margin-bottom:8px}
  .card-front .contact{font-size:6.5px;line-height:9px}
  .card-back{left:835px;background:var(--orange)}
  .card-back .quote{position:absolute;left:16px;top:26px;display:flex;gap:3px}
  .card-back .q{font-family:Georgia,serif;font-size:28px;line-height:22px;color:var(--paper)}
  .card-back .promo{font-size:9px;line-height:11px;color:var(--paper);width:120px;margin-top:4px}
  .card-back .trees{right:14px;bottom:14px;width:40px;height:34px;background:linear-gradient(90deg,var(--paper-shade) 0 40%,var(--green) 40%)}
</style>
</head>
<body>
<main class="canvas">

  <section class="sheet letterhead" aria-label="Letterhead">
    <div class="brand"><span class="brand-square"></span>Redfern Espresso</div>
    <p class="contact">1875 Heron Ridge Ave.<br>Pine Hollow, MN. 55990<br>T (651) 555-0142<br>E r_fern@quillpost.net</p>
    <div class="trees" role="img" aria-label="Pine tree illustration over orange and green blocks"></div>
    <p class="promo">Drive-thru to receive one free 12 oz. drink of choice!</p>
  </section>

  <section class="sheet envelope" aria-label="Envelope">
    <svg class="body" width="586" height="350" viewBox="0 0 586 350">
      <path d="M0 20 Q0 0 20 0 H566 Q586 0 586 20 V350 H0 Z" fill="#f4f0e4"/>
      <path d="M0 20 Q0 0 20 0 H566 Q586 0 586 20 V60 Q293 120 0 60 Z" fill="#c8602e"/>
    </svg>
    <div class="brand"><span class="brand-square"></span>Redfern Espresso</div>
    <p class="contact">1875 Heron Ridge Ave.<br>Pine Hollow, MN. 55990<br>T (651) 555-0142<br>E r_fern@quillpost.net</p>
    <div class="quote"><span class="q">“</span><p class="promo">Drive-thru to receive one free 12 oz. drink of choice!</p><span class="q">”</span></div>
    <div class="trees" role="img" aria-label="Pine tree illustration over orange and green blocks"></div>
    <div class="rule"></div>
  </section>

  <section class="sheet card card-front" aria-label="Business card front">
    <div class="brand"><span class="brand-square"></span>Redfern Espresso</div>
    <div class="person">
      <p class="name">Dale Ostrander</p>
      <p class="role">Manager</p>
      <p class="contact">1875 Heron Ridge Ave.<br>Pine Hollow, MN. 55990<br>T (651) 555-0142<br>E r_fern@quillpost.net</p>
    </div>
  </section>

  <section class="sheet card card-back" aria-label="Business card back">
    <div class="quote"><span class="q">“</span><p class="promo">Drive-thru to receive one free 12 oz. drink of choice!</p><span class="q">”</span></div>
    <div class="trees" role="img" aria-label="Pine tree illustration"></div>
  </section>

</main>
</body>
</html>
```